Business Stationary & Card Design

Double sided business cards, letterhead, horizontal brochure, and envelope design using our logo. We want a modern minimal look. One side of the business card should be only our logo and maybe our slogan "Get It Done Right". The other side should include our coil spring and not the logo again. Watermark like (or not) positioned partially, horizontal, on angle, or a combination of. IF a background color or accent color is used we like blue (4885ed). The letterhead, brochure, and envelope design should be similar to the card. Except no solid background color.Maybe the spring at the bottom of the letterhead page watermark style and partial. Additional info on the business card should be present:
Employee Name
Position
Phone
Email
Address
The final design should communicate strength, simplicity, and newness.

Target Market(s)

35-55 Male & Female

Industry/Entity Type

Automotive

Contact Information for Business Card

One side of the double sided business card should be only our logo and maybe our slogan "Get It Done Right". The other side should include our coil spring and not the logo again. Watermark like (or not) positioned partially, horizontal, on angle, or a combination of. IF a background color or accent color is used we like blue (4885ed). Additional info on the business card should be present:
Employee Name
Position
Phone
Email
Address

Font styles to use
Other font styles liked:
• Use font that compliments the attached font. Maybe plain eurostyle?

Colors
0492cd
3276b5

Requirements
Must have
• Use the coil spring in a subtle unique way (s). Double sided business card
Should not have
• Clutter, colors that do not coordinate well with our logo. Fonts that do not compliment our font.

```html
<!DOCTYPE html>
<html lang="en">
<head>
<meta charset="utf-8">
<title>Tensile Works Stationery</title>
<link href="https://fonts.googleapis.com/css2?family=Michroma&family=Open+Sans:wght@400;700&display=swap" rel="stylesheet">
<style>
:root{
  --bg:#d2d3d5;
  --paper:#ffffff;
  --blue:#577fc0;
  --gold:#d8b520;
  --ink:#3a3a3a;
  --muted:#6d6d6d;
  --faint:#f1f1f1;
}
*{margin:0;padding:0;box-sizing:border-box}
html,body{width:1200px;height:1200px;overflow:hidden;background:var(--bg)}
body{position:relative;font-family:"Open Sans",Arial,sans-serif;color:var(--ink)}
.sheet{position:absolute;background:var(--paper);box-shadow:0 4px 6px rgba(0,0,0,.12);overflow:hidden}
.wordmark{position:absolute;font-family:"Michroma",Arial,sans-serif;color:var(--gold);letter-spacing:.04em;text-align:center;line-height:1.05;white-space:nowrap}
.coil-area{position:absolute;background:linear-gradient(180deg,rgba(236,236,236,.75),rgba(244,244,244,.9))}
.contact{position:absolute;border-left:1.5px solid var(--gold);font-size:6px;line-height:7.5px;color:var(--ink)}
.contact div{display:flex;align-items:center;gap:4px;white-space:nowrap}
.contact svg{width:5px;height:5px;fill:var(--ink);flex:none}

/* letterhead */
.letterhead{left:101px;top:46px;width:443px;height:627px}
.letterhead .wordmark{left:0;right:0;top:70px;font-size:18px}
.letterhead .greeting{position:absolute;left:50px;top:164px;font-size:7.5px}
.letterhead .body{position:absolute;left:50px;top:202px;width:343px;font-size:7px;line-height:8.8px;color:var(--muted);text-align:justify}
.letterhead .body p{margin-bottom:9px}
.letterhead .body p.lead{font-weight:700;color:#444}
.signature{position:absolute;left:52px;top:432px;width:66px;height:16px;border-bottom:.8px solid #555}
.letterhead .coil-area{left:315px;top:390px;width:128px;height:237px}
.letterhead .contact.lines{left:52px;top:525px;padding-left:7px}
.letterhead .contact.addr{left:52px;top:562px;padding-left:7px}

/* business card */
.card-front{left:518px;top:115px;width:198px;height:114px;background:var(--blue)}
.card-front .wordmark{left:0;right:0;top:48px;font-size:11px}
.card-back{left:519px;top:238px;width:197px;height:112px}
.card-back .coil-area{left:140px;top:0;width:57px;height:112px}
.card-back .name{position:absolute;left:16px;top:21px;font-family:"Michroma",Arial,sans-serif;font-size:6px;color:#111}
.card-back .role{position:absolute;left:16px;top:30px;font-size:5px;color:var(--gold)}
.card-back .contact{font-size:3.6px;line-height:5px;padding-left:5px}
.card-back .contact svg{width:3.5px;height:3.5px}
.card-back .contact.lines{left:16px;top:50px}
.card-back .contact.addr{left:16px;top:81px}

/* envelope */
.envelope-back{left:564px;top:379px;width:479px;height:239px}
.flap{position:absolute;left:0;top:0;width:479px;height:82px}
.envelope-front{left:619px;top:562px;width:480px;height:240px}
.envelope-front .wordmark{left:40px;top:38px;font-size:17px;text-align:left}
.envelope-front .coil-area{left:360px;top:0;width:120px;height:240px}
.envelope-front .contact{font-size:6.4px;line-height:9.2px;padding-left:8px}
.envelope-front .contact.lines{left:40px;top:145px}
.envelope-front .contact.addr{left:40px;top:194px}

/* brochure */
.brochure{left:182px;top:835px;width:762px;height:269px}
.brochure .coil-area{left:245px;top:0;width:136px;height:269px}
.brochure .cover{position:absolute;left:381px;top:0;width:381px;height:269px;background:var(--blue);box-shadow:inset 14px 0 14px -10px rgba(0,0,0,.18)}
.brochure .cover .wordmark{left:0;right:0;top:120px;font-size:18px}
.brochure .contact{font-size:3px;line-height:4.6px;padding-left:4px}
.brochure .contact svg{width:3px;height:3px}
.brochure .contact.lines{left:40px;top:203px}
.brochure .contact.addr{left:40px;top:224px}
</style>
</head>
<body>
<svg width="0" height="0" style="position:absolute">
  <defs>
    <symbol id="i-phone" viewBox="0 0 10 10"><path d="M2 0.5l2 2-1 1.3c.6 1.3 1.6 2.3 2.9 2.9l1.3-1 2 2-1.4 1.8C4.3 9.2.8 5.7.5 2z"/></symbol>
    <symbol id="i-mail" viewBox="0 0 10 10"><path d="M0 2h10v6H0z M0 2l5 3.5L10 2" /></symbol>
    <symbol id="i-web" viewBox="0 0 10 10"><circle cx="5" cy="5" r="4.5"/></symbol>
    <symbol id="i-pin" viewBox="0 0 10 10"><path d="M5 0a3.5 3.5 0 0 1 3.5 3.5C8.5 6 5 10 5 10S1.5 6 1.5 3.5A3.5 3.5 0 0 1 5 0z"/></symbol>
  </defs>
</svg>

<!-- Letterhead -->
<section class="sheet letterhead">
  <div class="wordmark">TENSILE<br>WORKS</div>
  <p class="greeting">Dear, Mr_________</p>
  <div class="body">
    <p>Lorem Ipsum is simply dummy text of the printing and typesetting industry. Lorem Ipsum has been the industry's standard dummy text ever since the1500s,when an unknown printer took a galley of type and scrambled it to make a type specimen book. It has survived not only five centuries, but also the leap into electronic typesetting, remaining essentially unchanged. It was popularised in the 1960s with the release of Letraset sheets containing Lorem Ipsum passages,and more recently with desktop publishing software like Aldus PageMaker including versions of Lorem Ipsum.</p>
    <p class="lead">Lorem Ipsum is simply dummy text of the printing and typesetting industry. Lorem Ipsum has been the industry's standard dummy text ever since the1500s,when an unknown printer took a galley of type and scrambled it to make a type specimen book.</p>
    <p>Lorem Ipsum is simply dummy text of the printing and typesetting industry. Lorem Ipsum has been the industry's standard dummy text ever since the1500s,when an unknown printer took a galley of type and scrambled it to make a type specimen book. It has survived not only five centuries, but also the leap into electronic typesetting, remaining essentially unchanged.</p>
    <p>Lorem Ipsum is simply dummy text of the printing and typesetting industry. Lorem Ipsum has been the industry's standard dummy text ever since the1500s,when an unknown printer took a galley of type and scrambled it to make a type specimen book.</p>
    <p>Lorem Ipsum is simply dummy text of the printing and typesetting industry.</p>
  </div>
  <div class="signature" role="img" aria-label="Handwritten signature"></div>
  <div class="contact lines">
    <div><svg><use href="#i-phone"/></svg>+012-555-0147</div>
    <div><svg><use href="#i-mail"/></svg>info@tensileworks.com</div>
    <div><svg><use href="#i-web"/></svg>www.tensileworks.com</div>
  </div>
  <div class="contact addr"><div><svg><use href="#i-pin"/></svg>218 North Alder Ridge Road Fairhaven, NY 13064</div></div>
  <div class="coil-area" role="img" aria-label="Faint partial coil spring watermark"></div>
</section>

<!-- Business card front -->
<section class="sheet card-front">
  <div class="wordmark">TENSILE WORKS</div>
</section>

<!-- Business card back -->
<section class="sheet card-back">
  <div class="coil-area" role="img" aria-label="Faint partial coil spring watermark"></div>
  <p class="name">Marcus Hale</p>
  <p class="role">Agent</p>
  <div class="contact lines">
    <div><svg><use href="#i-phone"/></svg>+012-555-0147</div>
    <div><svg><use href="#i-mail"/></svg>info@tensileworks.com</div>
    <div><svg><use href="#i-web"/></svg>www.tensileworks.com</div>
  </div>
  <div class="contact addr">
    <div><svg><use href="#i-pin"/></svg>218 North Alder Ridge Road</div>
    <div style="padding-left:7.5px">Fairhaven, NY 13064</div>
  </div>
</section>

<!-- Envelope back -->
<section class="sheet envelope-back">
  <svg class="flap" viewBox="0 0 479 82" preserveAspectRatio="none">
    <path d="M0 0H479L472 68Q471 79 458 79H21Q9 79 8 68Z" fill="var(--blue)"/>
  </svg>
</section>

<!-- Envelope front -->
<section class="sheet envelope-front">
  <div class="coil-area" role="img" aria-label="Faint partial coil spring watermark"></div>
  <div class="wordmark">TENSILE<br>WORKS</div>
  <div class="contact lines">
    <div><svg><use href="#i-phone"/></svg>+012-555-0147</div>
    <div><svg><use href="#i-mail"/></svg>info@tensileworks.com</div>
    <div><svg><use href="#i-web"/></svg>www.tensileworks.com</div>
  </div>
  <div class="contact addr"><div><svg><use href="#i-pin"/></svg>218 North Alder Ridge Road Fairhaven, NY 13064</div></div>
</section>

<!-- Brochure -->
<section class="sheet brochure">
  <div class="coil-area" role="img" aria-label="Faint partial coil spring watermark"></div>
  <div class="contact lines">
    <div><svg><use href="#i-phone"/></svg>+012-555-0147</div>
    <div><svg><use href="#i-mail"/></svg>info@tensileworks.com</div>
    <div><svg><use href="#i-web"/></svg>www.tensileworks.com</div>
  </div>
  <div class="contact addr"><div><svg><use href="#i-pin"/></svg>218 North Alder Ridge Road Fairhaven, NY 13064</div></div>
  <div class="cover">
    <div class="wordmark">TENSILE<br>WORKS</div>
  </div>
</section>
</body>
</html>
```